Business Card Design Project

Looking for a cool, trendy design for new business cards for our Mobile Application business.

Quillmo Apps

www.quillmoapps.example

Target Market(s)

Looking for a bold modern design that attracts a younger demographic in the mobile space.

Industry/Entity Type

Business

Requirements
Must have
• Trendy, Easily adapted for other staff cards, works with large clients but showcases and innovative company

```html
<!DOCTYPE html>
<html lang="en">
<head>
<meta charset="utf-8">
<title>Quillmo Apps – Business Card</title>
<link rel="stylesheet" href="https://fonts.googleapis.com/css2?family=Courier+Prime&display=swap">
<style>
  :root {
    --stage-bg: #e9e6e1;
    --card-edge: #0b0b0d;
    --card-mid: #1f2024;
    --card-text: #8d8d8f;
  }
  html, body {
    margin: 0;
    padding: 0;
    width: 1200px;
    height: 1000px;
    overflow: hidden;
    background: var(--stage-bg);
  }
  .stage {
    width: 1200px;
    height: 1000px;
    display: flex;
    align-items: center;
    justify-content: center;
  }
  .business-card {
    width: 1000px;
    height: 567px;
    background: radial-gradient(ellipse 60% 65% at 52% 55%, var(--card-mid) 0%, #141518 55%, var(--card-edge) 100%);
    box-shadow: 0 10px 30px rgba(0, 0, 0, 0.35);
    display: flex;
    flex-direction: column;
    align-items: center;
    justify-content: center;
    font-family: "Courier Prime", "Courier New", monospace;
    color: var(--card-text);
  }
  .company-name {
    margin: 0;
    font-size: 52px;
    font-weight: 400;
    letter-spacing: 0;
    line-height: 1;
  }
  .tagline {
    margin: 22px 0 0;
    font-size: 14px;
    font-weight: 400;
    letter-spacing: 1px;
  }
</style>
</head>
<body>
  <main class="stage">
    <section class="business-card">
      <h1 class="company-name">Quillmo Apps</h1>
      <p class="tagline">~ Mobile software for professional development ~</p>
    </section>
  </main>
</body>
</html>
```